IT Consulting Business needs a web design

We need a web design for an IT Consulting company called "Verunex". We want to replace the existing web site (www.verunex-example.com) with a new design. Our services are IT Consulting, IT Training, IT Outsourcing.
We would like to see designs that communicate "Trusted IT Advisor" with modern & bold design.

We would like to see the design of 2 pages:
1. Home page (www.verunex-example.com)
2. The detail page (http://www.verunex-example.com/index_files/consulting.htm)

```html
<!DOCTYPE html>
<html lang="en">
<head>
<meta charset="utf-8">
<title>Verunex – Your Most Trusted IT Consultant</title>
<link href="https://fonts.googleapis.com/css2?family=Arimo:wght@400;700&family=PT+Sans:wght@400;700&display=swap" rel="stylesheet">
<style>
:root{
  --blue:#0054a6;
  --blue-dark:#004a93;
  --red:#e8141b;
  --text:#2b2b2b;
  --footer:#636466;
  --white:#ffffff;
  --rule:#a9a9a9;
}
*{margin:0;padding:0;box-sizing:border-box}
html,body{width:1051px;height:1200px;overflow:hidden;background:#fff}
body{font-family:"Arimo",Arial,sans-serif;color:var(--text)}
.page{position:relative;width:1051px;height:1200px;overflow:hidden;background:linear-gradient(#f1f1f3,#fff 110px)}
.abs{position:absolute}

/* header */
.brand{left:120px;top:38px;font:700 38px/1 "Arimo",sans-serif;color:var(--blue);letter-spacing:.5px}
.tagline{left:120px;top:86px;font:700 15.5px/1 "Arimo",sans-serif;color:var(--blue);letter-spacing:.3px}
.tagline em{font-style:normal;color:var(--red)}
.phone{left:802px;top:68px;display:flex;align-items:center;gap:6px;color:var(--red);font:18.5px/1 "PT Sans",sans-serif}

/* nav */
.nav{left:0;top:117px;width:1051px;height:46px;border-top:1px solid var(--blue);}
.nav-bar{position:absolute;left:0;top:3px;width:100%;height:42px;background:var(--blue);border-bottom:2px solid #fff;box-shadow:0 2px 0 var(--blue)}
.nav a{position:absolute;top:16px;color:#fff;text-decoration:none;font-size:13px}
.nav .sep{position:absolute;top:10px;width:1px;height:22px;background:#3b7bc0}

/* hero */
.hero{left:0;top:164px;width:1051px;height:324px;background:linear-gradient(90deg,#f4f5f7 0%,#e8e9ec 30%,#f7f7f8 45%,#d9dadd 70%,#eceef0 100%)}
.hero-caption{left:448px;top:445px;width:484px;height:32px;background:rgba(255,255,255,.8);font:21px/32px "PT Sans",sans-serif;color:#666;padding-left:5px}
.hero-caption span{color:var(--red)}

/* services */
.services{left:0;top:489px;width:1051px;height:165px;background:var(--blue)}
.services .divider{position:absolute;top:0;width:1px;height:165px;background:#1a63ad}
.service{position:absolute;top:12px;width:200px;color:#fff}
.service .icon{position:absolute;left:-1px;top:0;width:42px;height:42px;border-radius:50%;background:#fff;display:flex;align-items:center;justify-content:center}
.service h2{position:absolute;left:48px;top:18px;font:400 17px/1 "PT Sans",sans-serif;white-space:nowrap}
.service .rule{position:absolute;left:0;top:41px;width:186px;border-top:1px dotted #7fa8d6}
.service p{position:absolute;left:0;top:51px;width:186px;font-size:10.5px;line-height:15.8px;text-align:justify;text-align-last:justify}
.service .more{position:absolute;top:108px;width:75px;height:23px;background:#fff;color:#111;font-size:11px;line-height:23px;text-align:center;border:1px solid #ccc}

/* welcome */
.welcome h1{position:absolute;left:124px;top:689px;font:400 16.5px/1 "PT Sans",sans-serif;color:var(--blue)}
.welcome h1 span{color:var(--red)}
.welcome .rule{position:absolute;left:125px;top:725px;width:520px;border-top:1px dotted var(--rule)}
.welcome p{position:absolute;left:124px;width:521px;font-size:10.5px;line-height:15.8px;text-align:justify}
.welcome strong.lead{color:#1a5f9e}

/* expertise */
.expertise{left:682px;top:724px;width:271px;height:222px;background:linear-gradient(#f8f7f8,#ebeaeb);border:1px solid #dcdcdc}
.expertise h3{position:absolute;left:35px;top:22px;font:400 16.5px/1 "PT Sans",sans-serif;color:var(--blue)}
.expertise h3 span{color:var(--red)}
.expertise ul{list-style:none;position:absolute;left:16px;top:57px;width:245px}
.expertise li{height:31.5px;border-bottom:1px dotted #999;font-size:10.8px;line-height:31px;padding-left:20px;position:relative;color:#222}
.expertise li:last-child{border-bottom:none}
.expertise li::before{content:"»";position:absolute;left:3px;top:-1px;color:var(--blue);font-weight:700}

/* footer */
.footer{left:0;top:987px;width:1051px;height:156px;background:var(--footer);color:#fff}
.footer h4{position:absolute;top:32px;font:700 15px/1 "PT Sans",sans-serif;letter-spacing:.2px}
.footer .col{position:absolute;font-size:11px;line-height:15.8px}
.footer .social{position:absolute;left:816px;top:62px;display:flex;gap:9px}
.footer .social span{width:28px;height:28px;border-radius:50%;background:#fff}
.footer .brand-mark{position:absolute;left:815px;top:100px;font:700 24px/1 "Arimo",sans-serif;color:#fff}

.bottom{left:0;top:1143px;width:1051px;height:57px;background:var(--blue);border-top:2px solid #fff;color:#fff;font-size:11px}
.bottom .copy{position:absolute;left:120px;top:21px}
.bottom a,.bottom .dash{position:absolute;top:21px;color:#fff;text-decoration:none}
</style>
</head>
<body>
<div class="page">

  <header>
    <div class="abs brand">Verunex</div>
    <div class="abs tagline">Your Most Trusted <em>IT Consultant</em></div>
    <div class="abs phone">
      <svg width="26" height="32" viewBox="0 0 26 32" aria-hidden="true"><path d="M6 1c2 0 3 1 4 3l2 5c1 2 0 3-1 4l-2 2c1 4 4 8 7 10l2-2c1-1 3-1 4 0l3 4c1 2 0 3-1 4l-2 1c-3 1-7-1-11-6C7 21 3 13 2 8 1 5 3 2 6 1z" fill="#111"/></svg>
      <span>555-014-2290</span>
    </div>
  </header>

  <nav class="abs nav">
    <div class="nav-bar">
      <a style="left:123px">Home</a><span class="sep" style="left:184px"></span>
      <a style="left:206px">About Us</a><span class="sep" style="left:283px"></span>
      <a style="left:311px">Services</a><span class="sep" style="left:384px"></span>
      <a style="left:427px">Jobs</a><span class="sep" style="left:500px"></span>
      <a style="left:520px">Clinets Testimonials</a><span class="sep" style="left:659px"></span>
      <a style="left:698px">Contact Us</a>
    </div>
  </nav>

  <div class="abs hero" role="img" aria-label="Photo of a businessman drawing a system integration diagram on glass, colleagues blurred in the office background"></div>
  <div class="abs hero-caption">We Commit To What <span>Others Walk Away From</span></div>

  <section class="abs services">
    <span class="divider" style="left:377px"></span>
    <span class="divider" style="left:702px"></span>

    <div class="service" style="left:158px">
      <div class="icon"><svg width="26" height="22" viewBox="0 0 26 22" aria-hidden="true"><rect x="7" y="1" width="18" height="12" rx="2" fill="none" stroke="#555" stroke-width="1.6"/><rect x="1" y="6" width="17" height="11" rx="2" fill="#fff" stroke="#555" stroke-width="1.6"/><path d="M4 17l-1 4 5-4" fill="#fff" stroke="#555" stroke-width="1.6"/></svg></div>
      <h2>IT Consulting</h2>
      <div class="rule"></div>
      <p>Lorem Ipsum is simply dummy text of the printing and typesetting industry. Lorem Ipsum has been the industry's</p>
      <div class="more" style="left:55px">Read More</div>
    </div>

    <div class="service" style="left:454px">
      <div class="icon"><svg width="24" height="24" viewBox="0 0 24 24" aria-hidden="true"><rect x="3" y="4" width="14" height="16" rx="2" fill="none" stroke="#555" stroke-width="1.6"/><path d="M6 2v4M9 2v4M12 2v4" stroke="#555" stroke-width="1.6"/><path d="M7 12l3 3 5-6" fill="none" stroke="#555" stroke-width="1.8"/><path d="M16 18l5-5" stroke="#555" stroke-width="2"/></svg></div>
      <h2>IT Training</h2>
      <div class="rule"></div>
      <p>Lorem Ipsum is simply dummy text of the printing and typesetting industry. Lorem Ipsum has been the industry's</p>
      <div class="more" style="left:56px">Read More</div>
    </div>

    <div class="service" style="left:757px">
      <div class="icon"><svg width="26" height="26" viewBox="0 0 26 26" aria-hidden="true"><circle cx="13" cy="13" r="9" fill="#6b6b6b"/><ellipse cx="13" cy="13" rx="12" ry="4" fill="none" stroke="#333" stroke-width="1.4" transform="rotate(-20 13 13)"/></svg></div>
      <h2>IT Outsourcing</h2>
      <div class="rule"></div>
      <p>Lorem Ipsum is simply dummy text of the printing and typesetting industry. Lorem Ipsum has been the industry's</p>
      <div class="more" style="left:62px">Read More</div>
    </div>
  </section>

  <section class="welcome">
    <h1>WELCOME TO <span>VERUNEX</span></h1>
    <div class="rule"></div>
    <p style="top:743px"><strong class="lead">VERUNEX is most trusted&nbsp; IT Consultant of the printing and typesetting industry.</strong> <strong>Lorem Ipsum has been the</strong> industry's stantLorem Ipsum is simply dummy text of the printing and typesetting industry. Lorem Ipsum has been the industry's stantLorem Ipsum is simply dummy text of the printing and typesetting industry. Lorem Ipsum has been the industry's stantLorem Ipsum is simply dummy text of the printing and typesetting industry. Lorem um</p>
    <p style="top:822px">Lorem Ipsum is simply dummy text of the printing and typesetting industry. Lorem Ipsum has been the industry's stantLorem Ipsum is simply dummy text of the printing and typesetting industry. Lorem Ipsum has been the industry's stantLorem Ipsum is simply dummy text of the printing and typesetting industry. Lorem Ipsum has been the</p>
    <p style="top:885px">Lorem Ipsum has been the iLorem Ipsum has been the industry's stantLorem Ipsum is simply dummy text of the printing and typesettingLorem Ipsum has been the industry's stantLorem Ipsum is simply dummy text of the printing and typesettingLorem Ipsum has been the industry's stantLorem Ipsum is simply dummy text of the printing and typesettingLorem Ipsum has been the industry's stantLorem Ipsum is simply dummy text of the printing and</p>
  </section>

  <aside class="abs expertise">
    <h3>OUR <span>EXPERTISE</span></h3>
    <ul>
      <li>Portalis Collaboration Technologies</li>
      <li>Business Intelligence with Datavault Server</li>
      <li>Enterprise Integration with Linkwise Server</li>
      <li>Coreframe Development</li>
      <li>Flowstone Process Suite</li>
    </ul>
  </aside>

  <footer class="abs footer">
    <h4 style="left:125px">ADDRESS</h4>
    <div class="col" style="left:126px;top:62px">18/7 MARLOW LANE, KESTON RD.,<br>ARDEL, NORTHVALE,<br>NORTHVALE 20410<br>ELANDIA</div>

    <h4 style="left:486px">CONTACT US</h4>
    <div class="col" style="left:488px;top:58px">Please do not hesitate to get in contact with us.</div>
    <div class="col" style="left:488px;top:80px;font-weight:700">Phone: 02-555-0147<br>Fax: 02-555-0198<br>E-mail: info@verunex-example.com</div>

    <h4 style="left:816px">FOLLOW US</h4>
    <div class="social"><span></span><span></span><span></span></div>
    <div class="brand-mark">Verunex</div>
  </footer>

  <div class="abs bottom">
    <span class="copy">Copyright (C)Verunex 2013 - 2014 .&nbsp; All Rights Reserved</span>
    <a style="left:483px">Home</a><span class="dash" style="left:532px">-</span>
    <a style="left:558px">Aboout Us</a><span class="dash" style="left:637px">-</span>
    <a style="left:660px">Services</a><span class="dash" style="left:722px">-</span>
    <a style="left:739px">jobs</a><span class="dash" style="left:777px">-</span>
    <a style="left:791px">Testimonials</a><span class="dash" style="left:870px">-</span>
    <a style="left:887px">Contact Us</a>
  </div>

</div>
</body>
</html>
```